Veltrano - Mechanic/Collision Center Business Card

We're looking for a business card design for our mechanic/ collision repair shop.

Can be with colours or monochromatic.

See the attached files.

Many thanks

```html
<!DOCTYPE html>
<html lang="pt">
<head>
<meta charset="utf-8">
<title>Veltrano – Business Card</title>
<link href="https://fonts.googleapis.com/css2?family=Arimo:wght@400;700&display=swap" rel="stylesheet">
<style>
  :root{
    --stage:#3e414a;
    --ink:#1b1e22;
    --blue:#1e9bd7;
    --blue-deep:#1777a8;
    --paper:#ffffff;
    --rule:#a9acb0;
  }
  html,body{margin:0;padding:0;}
  body{
    width:1200px;height:675px;overflow:hidden;
    background:var(--stage);
    font-family:"Arimo",Arial,sans-serif;
    display:flex;align-items:center;justify-content:center;gap:48px;
  }
  .card{
    position:relative;width:530px;height:303px;overflow:hidden;
    box-shadow:0 14px 30px rgba(0,0,0,.35);
  }
  .card svg.art{position:absolute;inset:0;width:100%;height:100%;}

  /* front */
  .brand{
    position:absolute;display:flex;align-items:center;gap:8px;
    font-weight:700;letter-spacing:.5px;
  }
  .front .brand{left:26px;top:92px;font-size:34px;color:var(--ink);}
  .brand-dot{width:14px;height:14px;border-radius:50%;background:var(--blue);flex:none;}
  .holder{
    position:absolute;right:22px;top:54px;
    color:var(--paper);font-weight:700;font-size:21px;letter-spacing:1.5px;
  }
  .contacts{
    position:absolute;right:22px;top:108px;
    list-style:none;margin:0;padding:0;
    color:var(--ink);font-size:14px;line-height:1.25;text-align:right;
  }
  .contacts li{display:flex;justify-content:flex-end;align-items:flex-start;gap:6px;margin-bottom:7px;}
  .contacts .icon{width:14px;height:14px;flex:none;margin-top:1px;}

  /* back */
  .back .brand{left:50%;top:50%;transform:translate(-50%,-70%);font-size:42px;color:var(--paper);}
  .back .brand-dot{background:var(--paper);width:18px;height:18px;}
</style>
</head>
<body>

<section class="card front" aria-label="Card front">
  <svg class="art" viewBox="0 0 530 303" preserveAspectRatio="none" aria-hidden="true">
    <rect width="530" height="303" fill="var(--blue)"/>
    <polygon points="0,0 250,0 250,18 95,303 0,303" fill="var(--paper)"/>
    <polygon points="250,18 262,18 107,303 95,303" fill="var(--rule)"/>
    <polygon points="40,0 250,0 250,18" fill="var(--ink)"/>
    <polygon points="0,250 40,303 0,303" fill="var(--ink)"/>
    <polygon points="262,50 530,50 530,88 242,88" fill="var(--ink)"/>
    <polygon points="242,88 530,88 530,100 236,100" fill="var(--blue-deep)"/>
    <polygon points="110,303 530,303 530,290 116,290" fill="var(--ink)"/>
  </svg>
  <div class="brand"><span class="brand-dot"></span>VELTRANO</div>
  <div class="holder">RUI MATOS</div>
  <ul class="contacts">
    <li><span>Veltrano, LDA<br>Rua do Sol Nascente, 42<br>2400-118 Leiria</span>
      <svg class="icon" viewBox="0 0 14 14"><circle cx="7" cy="7" r="7" fill="var(--ink)"/><path d="M7 3a2.6 2.6 0 0 0-2.6 2.6C4.4 7.6 7 11 7 11s2.6-3.4 2.6-5.4A2.6 2.6 0 0 0 7 3z" fill="var(--blue)"/><circle cx="7" cy="5.6" r="1" fill="var(--ink)"/></svg></li>
    <li><span>+351 910 000 482</span>
      <svg class="icon" viewBox="0 0 14 14"><circle cx="7" cy="7" r="7" fill="var(--ink)"/><path d="M4.6 3.6l1.4 1.6-.8 1a5 5 0 0 0 2.6 2.6l1-.8 1.6 1.4-.8 1.2C6.6 10.4 3.6 7.4 3.4 4.4z" fill="var(--blue)"/></svg></li>
    <li><span>veltrano.oficina@mail.pt</span>
      <svg class="icon" viewBox="0 0 14 14"><circle cx="7" cy="7" r="7" fill="var(--ink)"/><rect x="3.5" y="4.6" width="7" height="4.8" fill="none" stroke="var(--blue)" stroke-width="1"/><path d="M3.5 4.6L7 7.4l3.5-2.8" fill="none" stroke="var(--blue)" stroke-width="1"/></svg></li>
    <li><span>www.veltrano-oficina.pt</span>
      <svg class="icon" viewBox="0 0 14 14"><circle cx="7" cy="7" r="7" fill="var(--ink)"/></svg></li>
  </ul>
</section>

<section class="card back" aria-label="Card back">
  <svg class="art" viewBox="0 0 530 303" preserveAspectRatio="none" aria-hidden="true">
    <rect width="530" height="303" fill="var(--ink)"/>
    <polygon points="150,0 190,0 190,150 150,150" fill="var(--blue)"/>
    <polygon points="0,200 150,150 360,150 530,240 530,303 0,303" fill="var(--blue)"/>
  </svg>
  <div class="brand"><span class="brand-dot"></span>VELTRANO</div>
</section>

</body>
</html>
```